Harbor Sushi & Steak Dinner Menu

I'm looking for a MENU design with a particular feel. I want to have a base template made that I can then use for future alterations to the menu; ie I can go in and change out different entrees as the menu changes but the template will remain the same. (Ideally it would be in an Apple Pages format.). Also ideally - dinner menu will occupy 2 pages 8.5 x 11. The restaurant's name is Harbor. It is a MODERN steak house that will also feature Sushi, a Raw Bar, Exquisite Cocktails and a sophisticated nightlife crowd. I have attached our LOGO, a secondary logo that we will be featuring throughout the project including on the menu cover (the gold U). Finally - I have attached the content that we would like to see. AGAIN - I REITERATE: High end dining and lounge atmosphere. A couple of restaurants / menus that I love are Morvendel in NYC and Pellucid Steakhouse in Long Island NY. Please do not duplicate - just trying to offer some suggestions.

Requirements
Must have
• A sophisticated and elegant feel without being stuffy or old.

```html
<!DOCTYPE html>
<html lang="en">
<head>
<meta charset="utf-8">
<title>Harbor Sushi &amp; Steak — Dinner Menu</title>
<link rel="stylesheet" href="https://fonts.googleapis.com/css2?family=Montserrat:wght@400;500;600;700;800&family=Oswald:wght@300;400&display=swap">
<style>
:root{
  --red:#b51f2e;
  --gold:#c9ad5f;
  --ink:#1e1e1e;
  --paper:#f6f5f2;
  --backdrop:#e4e1db;
}
*{box-sizing:border-box;margin:0;padding:0}
html,body{width:895px;height:1200px;overflow:hidden;background:var(--backdrop)}
body{position:relative;font-family:"Montserrat",sans-serif;color:var(--ink)}
.page{position:absolute;width:395px;height:500px;background:var(--paper);overflow:hidden;box-shadow:0 2px 8px rgba(0,0,0,.12)}
.page--cover{left:40px;top:80px}
.page--sushi{left:460px;top:80px}
.page--kitchen{left:40px;top:620px}
.page--sides{left:460px;top:620px}
.wave{position:absolute;left:0;bottom:0;width:100%;height:60px;display:block}

/* brand name */
.brand{display:flex;align-items:center;justify-content:center;gap:8px;color:var(--gold);font-weight:500;letter-spacing:.18em;text-transform:uppercase}
.brand__dot{width:9px;height:9px;border-radius:50%;background:var(--red)}
.page--cover .brand{position:absolute;top:190px;left:0;right:0;font-size:34px}
.page--sushi .brand{margin:22px 0 14px;font-size:22px}
.cover-title{position:absolute;top:345px;left:0;right:0;text-align:center;color:var(--gold);font-weight:800;font-size:20px;line-height:1.25;letter-spacing:.01em}
.cover-rule{position:absolute;top:408px;left:50%;width:68px;margin-left:-34px;height:2px;background:var(--red)}

/* columns */
.columns{display:flex;padding:0 24px}
.col{flex:1}
.col + .col{border-left:1px dashed #777;padding-left:16px;margin-left:8px}
.page--kitchen .columns{padding-top:32px}
.page--sides .columns{padding-top:62px}

/* section headings */
.heading{display:inline-block;position:relative;font-family:"Oswald",sans-serif;font-weight:300;font-size:14px;letter-spacing:.04em;color:var(--gold);text-transform:uppercase;border:1px solid var(--red);padding:0 10px;line-height:17px;margin:0 0 6px}
.heading::before,.heading::after{content:"";position:absolute;top:3px;width:4px;height:9px;border:1px solid var(--red)}
.heading::before{left:-5px;border-right:none}
.heading::after{right:-5px;border-left:none}
.heading--small{font-size:10.5px;line-height:14px;padding:0 8px}
.heading--plain{color:var(--ink);font-weight:400;font-size:10px}
.heading--plain::before,.heading--plain::after{display:none}
.section{margin-bottom:9px}

/* items */
.item{font-size:6.6px;line-height:1.28;margin-bottom:3.5px}
.item b{color:var(--red);font-weight:700}
.gf{color:var(--red);font-weight:700}
.item--caps{text-transform:uppercase;font-weight:600;margin-bottom:1.5px}
.dish{font-size:6.6px;line-height:1.28;margin-bottom:4px}
.dish__name{display:block;font-weight:500}
.dish__name--red{color:var(--red)}
.dish__desc{display:block}
.list{list-style:none;font-size:6.6px;line-height:1.55;text-transform:uppercase;font-weight:500}
.list--bold{font-weight:700}
.note{font-size:5.6px;color:var(--red)}
.desserts{margin-top:10px;font-size:6.6px}
.desserts strong{display:block;font-size:7.5px;font-weight:700;margin-bottom:2px}

.venue-photo{position:absolute;left:0;right:0;bottom:0;height:230px;background:linear-gradient(180deg,var(--paper) 0%,#d9cfa4 18%,#e2a34b 35%,#6b6a70 55%,#1d2a6b 75%,#0e1438 100%)}
</style>
</head>
<body>

<section class="page page--cover">
  <div class="brand"><span class="brand__dot"></span>Harbor</div>
  <h1 class="cover-title">HARBOR SUSHI &amp; STEAK<br>DINNER MENU</h1>
  <div class="cover-rule"></div>
  <svg class="wave" viewBox="0 0 400 60" preserveAspectRatio="none" aria-hidden="true">
    <path d="M0 60 L0 44 C120 16 260 8 400 26 L400 60Z" fill="var(--red)"/>
    <path d="M0 36 C120 6 260 -2 400 16" fill="none" stroke="var(--gold)" stroke-width="4"/>
  </svg>
</section>

<section class="page page--sushi">
  <div class="brand"><span class="brand__dot"></span>Harbor</div>
  <div class="columns">
    <div class="col">
      <div class="section">
        <h2 class="heading">Sushi / Sashimi</h2>
        <p class="item"><b>TORO</b> - blue fin tuna belly <span class="gf">(GF)</span></p>
        <p class="item"><b>EBI</b> - cooked shrimp <span class="gf">(GF)</span></p>
        <p class="item"><b>HAMACHI</b> - yellowtail <span class="gf">(GF)</span></p>
        <p class="item"><b>UNI</b> - sea urchin <span class="gf">(GF)</span></p>
        <p class="item"><b>HIRAME</b> - fluke <span class="gf">(GF)</span></p>
        <p class="item"><b>UNAGI</b> - fresh water eel <span class="gf">(GF)</span></p>
        <p class="item"><b>SAKE</b> - salmon <span class="gf">(GF)</span></p>
        <p class="item"><b>MADAI</b> - red snapper <span class="gf">(GF)</span></p>
        <p class="item"><b>MAGURO</b> - tuna <span class="gf">(GF)</span></p>
      </div>
      <div class="section">
        <h2 class="heading">Sushi Platters</h2>
        <p class="item"><b>SMALL</b> - Five Pieces assorted sushi, nine pieces sashimi, spicy tuna roll <span class="gf">(GF)</span></p>
        <p class="item"><b>LARGE</b> - Eight Pieces assorted sushi, eighteen pieces of sashimi, alaskan roll, rainbow roll <span class="gf">(GF)</span></p>
      </div>
      <div class="section">
        <h2 class="heading">Classic Rolls</h2>
        <p class="item"><b>YELLOWTAIL</b>- inside out roll with scallions <span class="gf">(GF)</span></p>
        <p class="item"><b>SPICY TUNA OR SALMON OR YELLOWTAIL</b> - spicy mayo <span class="gf">(GF)</span></p>
        <p class="item"><b>CALIFORNIA</b> - crab meat, cucumber and avocado <span class="gf">(GF)</span></p>
        <p class="item"><b>VEGETABLE</b> - avocado, cucumber, asparagus and pickled reddish <span class="gf">(GF)</span></p>
      </div>
    </div>
    <div class="col">
      <div class="section">
        <p class="item"><b>SPIDER</b> - soft shell crab and avocado with eel sauce</p>
        <p class="item"><b>SHRIMP TEMPURA</b> - deep fried tempura shrimp and eel sauce</p>
        <p class="item"><b>ALASKAN</b> - salmon and avocado <span class="gf">(GF)</span></p>
      </div>
      <div class="section">
        <h2 class="heading">Special Rolls</h2>
        <p class="item"><b>THE HARBOR</b> - tuna, salmon, yellowtail, avocado, spicy mayo, soy bean paper</p>
        <p class="item"><b>KING CRAB RAINBOW</b> - king crab, avocado, cucumbers, assorted fish on top</p>
        <p class="item"><b>EMPRESS</b> - Shrimp tempura, spicy tuna on top, eel sauce, spicy mayo</p>
        <p class="item"><b>SPICY GIRL</b> - Spicy crunchy crab meat, cucumber, shrimp on top</p>
        <p class="item"><b>DRAGON</b> - Eel, cucumber, avocado, and tobiko on top, eel sauce</p>
        <p class="item"><b>YUMMY</b> - spicy crunchy salmon, avocado, mango and salmon on top</p>
        <p class="item"><b>NO. 9</b> - Shrimp Tempura, avocado, kani, spicy mayo, tobiko</p>
        <p class="item"><b>SUNRISE ROLL</b> - spicy crunchy tuna and avocado, spicy crunchy salmon on top</p>
      </div>
      <div class="section">
        <h2 class="heading">Seafood Raw Bar</h2>
        <ul class="list list--bold">
          <li>Lobster Cocktail</li><li>Shrimp Cocktail</li><li>Clams on the Half Shell</li><li>Oysters on the Half Shell</li><li>Colossal Crab Cocktail</li>
        </ul>
      </div>
    </div>
  </div>
  <svg class="wave" viewBox="0 0 400 60" preserveAspectRatio="none" aria-hidden="true">
    <path d="M0 60 L0 36 C120 50 260 14 400 22 L400 60Z" fill="var(--red)"/>
    <path d="M0 30 C130 44 260 4 400 12" fill="none" stroke="var(--gold)" stroke-width="4"/>
  </svg>
</section>

<section class="page page--kitchen">
  <div class="columns">
    <div class="col">
      <div class="section">
        <h2 class="heading heading--small">Raw Bar Plate for One:</h2>
        <p class="dish"><span class="dish__desc">Two Shrimp, Half of a One Pound Lobster, Two Clams, One East Coast Oyster, One West Coast Oyster</span></p>
      </div>
      <div class="section">
        <h2 class="heading heading--small">Seafood Platters <span class="gf">(GF)</span></h2>
        <p class="dish"><span class="dish__desc">Shrimp, Oysters, Clams, Lobster and Crab</span><span class="dish__desc">LARGE OR COLOSSAL</span></p>
      </div>
      <div class="section">
        <h2 class="heading heading--small">Apps</h2>
        <p class="dish"><span class="dish__name">BAO Bun; hoisin bbq pancetta cut pork loin, crispy onions, micro mint</span></p>
        <p class="dish"><span class="dish__name">Five Spice Crispy Popcorn Crusted Prawns (2)</span><span class="dish__desc">classic burre blanc</span></p>
        <p class="dish"><span class="dish__name">Crispy Wonton Napoleon</span><span class="dish__desc">cucumber gallete, ahi tuna, jumbo lump crab meat, wasabi aioli, shoestring wontons</span></p>
        <p class="dish"><span class="dish__name">PEI Mussels</span><span class="dish__desc">PEI Mussels; charred artichoke hearts, blistered heirloom tomatoes, garlic white wine broth</span></p>
        <p class="dish"><span class="dish__name">New Zealand or Domestic Small Eye Lamb Chop (1)</span><span class="dish__desc">crispy porcini risotto cake</span></p>
      </div>
      <div class="section">
        <h2 class="heading heading--small">Salads</h2>
        <p class="dish"><span class="dish__name">Classic Wedge</span><span class="dish__desc">bleu cheese, bacon lardons, heirloom tomatoes</span></p>
        <p class="dish"><span class="dish__name">Mixed Baby Greens</span><span class="dish__desc">heirloom tomatoes, cucumber, red onion, dijon vinaigrette</span></p>
        <p class="dish"><span class="dish__name">Tabulleh</span><span class="dish__desc">buckwheat grain, fresh mint, tomato concasse, cucumber, parsley, fresh squeezed lemon, EVOO., salt and pepper</span></p>
        <p class="note">Tomato Mozzarella Salad / Burratta</p>
      </div>
    </div>
    <div class="col">
      <div class="section">
        <p class="dish"><span class="dish__name">Spinach Salad</span><span class="dish__desc">green apple, feta, currants, with per-simmons vinaigrette</span></p>
        <p class="dish"><span class="dish__name">Kale Caesar</span><span class="dish__desc">homemade cacio e'peppe dressing, pecorino and parmesan cheese, toasted croutons.</span></p>
      </div>
      <div class="section">
        <h2 class="heading">Entrees</h2>
        <p class="dish"><span class="dish__name">Pan Roasted Miso Glazed Black Cod</span><span class="dish__desc">green tea noodle stir fry; Napa cabbage, carrot, Japanese eggplant</span></p>
        <p class="dish"><span class="dish__name">Pan Seared Striped Bass;</span><span class="dish__desc">lobster succotash in a tomato saffron broth</span></p>
        <p class="dish"><span class="dish__name dish__name--red">E.V.O.O. Salted / Grilled Swordfish;</span><span class="dish__desc">un dried tomato, olive and caper tapenade, over basmati rice</span></p>
        <p class="dish"><span class="dish__name dish__name--red">Grilled Half Chicken;</span><span class="dish__desc">sun dried tomato and basil Israeli cous-cous, pan au jus</span></p>
        <p class="dish"><span class="dish__name dish__name--red">Roasted Fresh Caviatelle Ratatoille</span><span class="dish__desc">vegetable broth</span></p>
        <p class="dish"><span class="dish__name dish__name--red">Lobster Cartoccio;</span><span class="dish__desc">shrimp, mussels, clams, fresh herb tomato broth, tossed with bucatini</span></p>
        <p class="dish"><span class="dish__desc">Charred Artichoke Hearts, heirloom tomatoes, caper berries, spring onions, fresh basil, white wine reduction over forbidden rice (gf)</span></p>
        <p class="dish"><span class="dish__name">Mediterranean Grilled Veggie Plate</span><span class="dish__desc">Artichoke hearts, Japanese eggplant, green &amp; white asparagus, seared heirloom tomatoes, roasted baby carrots, cauliflower rice, evoo &amp; fig drizzle (gf)</span></p>
      </div>
      <div class="section">
        <h2 class="heading heading--small">USDA Prime Steaks (gf)</h2>
        <ul class="list list--bold">
          <li>10 oz Filet</li><li>14 or 16 oz New York Strip</li><li>24 oz Boneless Ribeye</li><li>36 oz Bone in Rib Eye</li><li>36 oz Bone in Rib Eye</li>
        </ul>
      </div>
    </div>
  </div>
  <svg class="wave" viewBox="0 0 400 60" preserveAspectRatio="none" aria-hidden="true">
    <path d="M0 60 L0 50 C120 28 260 8 400 30 L400 60Z" fill="var(--red)"/>
    <path d="M0 40 C120 18 260 -2 400 18" fill="none" stroke="var(--gold)" stroke-width="4"/>
  </svg>
</section>

<section class="page page--sides">
  <div class="venue-photo" role="img" aria-label="Photo of the lounge bar with a colourful mural wall, screens and blue-lit bar stools"></div>
  <div class="columns">
    <div class="col">
      <h2 class="heading heading--plain">Sauces</h2>
      <ul class="list">
        <li>Cabernet Demi Glaz</li><li>Gorganzola Brulle Cream</li><li>Truffled Wild Mushroom Ragum</li><li>Horseradish Cream</li><li>House Steak Sauce</li>
      </ul>
      <p class="desserts"><strong>DESSERTS</strong>T.B.D. - SEPARATE MENU</p>
    </div>
    <div class="col">
      <h2 class="heading heading--plain">Sides</h2>
      <ul class="list">
        <li>Mashed Idaho Potatoes</li><li>Bacon, Sweet Corn, Caramelized Vidalia Onion Fingerling Potatoes</li><li>Roasted Peanut Potatoes</li><li>Creamed Spinach</li><li>Sautéed Spinach</li><li>Grilled Asparagus</li><li>French Beans</li><li>Israeli Cous Cous</li><li>Sweet Potato Steak Fries</li><li>Corn Skillet</li>
      </ul>
    </div>
  </div>
  <svg class="wave" viewBox="0 0 400 60" preserveAspectRatio="none" aria-hidden="true">
    <path d="M0 14 C120 40 260 10 400 26 L400 0 L0 0Z" fill="var(--paper)"/>
    <path d="M0 60 L0 34 C120 52 260 16 400 28 L400 60Z" fill="var(--red)"/>
    <path d="M0 26 C120 46 260 8 400 18" fill="none" stroke="var(--gold)" stroke-width="4"/>
  </svg>
</section>

</body>
</html>
```